Business Card Trio Design

We need a set of business cards that all match but are not identical. We need one generic for the business and one for each of the two owners. We would like the cards to be similar to each other, but not identical. We have a logo and the colors of the logo are painstakingly chosen so if blue or green is used, we prefer our specific blue and green. Our logo pops better on a black background as well. We are open to double-sided, but it is not the top choice. We would love some either gold or silver accents that are in a foiled appearance. We sell uniforms (scrubs, culinary, EMT, police, fire, business, all types except kids and sports), shoes, equipment, and accessories. We also have quorvalink, mavelgrid, lumopixel, and yondrel that we would like to have them follow and we offer zembrix in the store we would like the card to also advertise.

```html
<!DOCTYPE html>
<html lang="en">
<head>
<meta charset="utf-8">
<title>Verdant Apparel – Business Cards</title>
<link href="https://fonts.googleapis.com/css2?family=Lato:wght@300;400&display=swap" rel="stylesheet">
<style>
  :root {
    --backdrop: #1f1f1f;
    --card: #262626;
    --card-edge: #0e4a38;
    --silver: #d4d4d4;
    --brand-green: #16a37a;
    --brand-blue: #7ea3c6;
    --text-light: #c9c9c9;
  }
  * { margin: 0; padding: 0; box-sizing: border-box; }
  html, body {
    width: 1200px; height: 958px; overflow: hidden;
    background: var(--backdrop);
    font-family: 'Lato', sans-serif;
  }
  .canvas {
    width: 1200px; height: 958px;
    display: flex; align-items: center; justify-content: center; gap: 60px;
  }
  .card {
    position: relative;
    width: 525px; height: 300px;
    background: var(--card);
    border-bottom: 6px solid var(--card-edge);
    box-shadow: 0 18px 40px rgba(0,0,0,.55);
    overflow: hidden;
  }
  .card--front { display: flex; align-items: center; justify-content: center; }
  .wordmark {
    display: flex; align-items: center; gap: 18px;
    font-weight: 300; letter-spacing: .12em; text-transform: uppercase;
  }
  .wordmark__dot { width: 56px; height: 56px; border-radius: 50%; }
  .wordmark__name { font-size: 40px; line-height: 1; }
  .card--front .wordmark { color: var(--silver); }
  .card--front .wordmark__dot { background: var(--silver); }

  .card--back .wordmark {
    position: absolute; left: 40px; top: 40px; gap: 12px; color: var(--brand-green);
  }
  .card--back .wordmark__dot { width: 30px; height: 30px; background: var(--brand-blue); }
  .card--back .wordmark__name { font-size: 24px; }

  .address {
    position: absolute; right: 40px; top: 40px;
    text-align: right; color: var(--text-light);
    font-size: 13px; line-height: 1.6; font-weight: 300;
  }
  .contact {
    position: absolute; left: 40px; bottom: 36px;
    list-style: none; color: var(--text-light);
    font-size: 14px; font-weight: 300; line-height: 1.9;
  }
  .contact li { display: flex; align-items: center; gap: 10px; }
  .contact svg { width: 14px; height: 14px; fill: none; stroke: var(--brand-green); stroke-width: 2; }
</style>
</head>
<body>
<main class="canvas">
  <section class="card card--front" aria-label="Card front">
    <div class="wordmark">
      <span class="wordmark__dot"></span>
      <span class="wordmark__name">Verdant Apparel</span>
    </div>
  </section>

  <section class="card card--back" aria-label="Card back">
    <div class="wordmark">
      <span class="wordmark__dot"></span>
      <span class="wordmark__name">Verdant Apparel</span>
    </div>
    <address class="address" style="font-style:normal">
      Verdant Apparel<br>48 Harlow Court<br>Brookfield, NC 27000
    </address>
    <ul class="contact">
      <li><svg viewBox="0 0 24 24"><path d="M5 3h4l2 5-3 2a12 12 0 0 0 6 6l2-3 5 2v4a2 2 0 0 1-2 2A18 18 0 0 1 3 5a2 2 0 0 1 2-2z"/></svg>(555) 014-2287</li>
      <li><svg viewBox="0 0 24 24"><rect x="3" y="5" width="18" height="14" rx="1"/><path d="M3 6l9 7 9-7"/></svg>hello@verdantapparel.com</li>
      <li><svg viewBox="0 0 24 24"><circle cx="12" cy="12" r="9"/><path d="M3 12h18M12 3c3 3 3 15 0 18M12 3c-3 3-3 15 0 18"/></svg>www.verdantapparel.com</li>
    </ul>
  </section>
</main>
</body>
</html>
```